A Speech Therapy Business needs to update their logo

I need an update to the font and color of my logo to look more appealing. I am looking to open a private practice as a Speech Language Pathologist that caters to adults and children. It needs to be sophisticated and friendly at the same time. I want to keep the silhouette in my logo as is, just update the font and color for "Brightpaths".
Industry/Entity Type
Business
Contact Information for Business Card
I want the business card to have my logo, my name (Dorota Valk, CCC-SLP, TSSLD) and that I am a Bilingual Speech Language Pathologist. Also, include my phone number, (555) 271-8390. Include my website, Brightpathsslp.example, and email address, dorotavalk@brightpathsslp.example
Look and feel
Each slider illustrates characteristics of the customer's brand and the style your logo design should communicate.

```html
<!DOCTYPE html>
<html lang="en">
<head>
<meta charset="utf-8">
<title>Brightpaths – Business Card</title>
<link href="https://fonts.googleapis.com/css2?family=Questrial&display=swap" rel="stylesheet">
<style>
  :root {
    --page: #ffffff;
    --card: #f4f4f4;
    --teal: #2bb5a0;
    --ink: #2b2b2b;
    --charcoal: #3a3a3a;
    --silhouette: #4a4a4a;
    --ribbon: #e9e5e4;
    --ribbon-shade: #d9d3d1;
  }
  * { box-sizing: border-box; margin: 0; padding: 0; }
  html, body {
    width: 1200px; height: 900px; overflow: hidden;
    background: var(--page);
    font-family: "Questrial", "Century Gothic", sans-serif;
  }
  .business-card {
    position: absolute; left: 100px; top: 165px;
    width: 1000px; height: 570px;
    border-radius: 34px; overflow: hidden;
    background: linear-gradient(160deg, #fbfbfb 0%, var(--card) 45%, #ececec 100%);
    box-shadow: 0 24px 50px rgba(0,0,0,.16);
  }
  .background-facets {
    position: absolute; inset: 0;
    background:
      linear-gradient(125deg, rgba(255,255,255,0) 0%, rgba(230,230,230,.45) 35%, rgba(255,255,255,0) 55%),
      linear-gradient(60deg, rgba(255,255,255,0) 50%, rgba(222,222,222,.4) 75%, rgba(255,255,255,0) 100%);
  }
  .ghost-figures {
    position: absolute; left: 0; top: 200px; width: 900px; height: 300px;
    background: radial-gradient(closest-side, rgba(190,190,190,.45) 0%, rgba(205,205,205,.2) 55%, rgba(235,235,235,0) 100%);
  }
  .logo-figures {
    position: absolute; left: 58px; top: 55px; width: 440px; height: 130px;
    border-radius: 60px 60px 24px 24px;
    background: linear-gradient(90deg, rgba(74,74,74,.55) 0%, rgba(74,74,74,.35) 60%, rgba(74,74,74,.18) 100%);
    clip-path: polygon(0 8%, 45% 20%, 75% 45%, 100% 62%, 100% 100%, 0 100%);
  }
  .logo-name {
    position: absolute; left: 50px; top: 198px;
    font-size: 96px; line-height: 1; color: var(--teal);
  }
  .practitioner {
    position: absolute; right: 62px; top: 48px; text-align: right;
  }
  .practitioner-name { font-size: 28px; color: var(--teal); }
  .practitioner-name .credentials { font-size: 16px; }
  .practitioner-title { margin-top: 4px; font-size: 16px; color: var(--ink); }
  .contact-list {
    position: absolute; left: 600px; top: 365px; list-style: none;
    font-size: 19px; color: var(--ink);
  }
  .contact-list li { display: flex; align-items: center; gap: 6px; height: 28px; }
  .contact-list svg { width: 20px; height: 20px; flex: none; }
  .waves { position: absolute; left: 0; top: 0; width: 1000px; height: 570px; }
</style>
</head>
<body>
  <div class="business-card">
    <div class="background-facets" role="img" aria-label="Soft grey faceted polygon background pattern"></div>
    <div class="ghost-figures" role="img" aria-label="Faint grey silhouettes of a family holding hands"></div>

    <svg class="waves" viewBox="0 0 1000 570" aria-hidden="true">
      <path d="M0 420 C 200 360, 420 390, 560 470 C 640 515, 700 540, 760 570 L 700 570 C 600 520, 480 440, 300 420 C 180 405, 80 420, 0 445 Z" fill="var(--ribbon)"/>
      <path d="M0 398 C 150 375, 300 385, 420 430 L 410 436 C 290 395, 150 390, 0 410 Z" fill="var(--teal)"/>
      <path d="M0 425 C 160 405, 330 420, 450 470 C 520 500, 570 535, 600 570 L 540 570 C 500 520, 430 480, 330 458 C 220 435, 100 440, 0 470 Z" fill="var(--charcoal)"/>
      <path d="M560 570 C 650 520, 760 505, 1000 455 L 1000 478 C 790 520, 680 540, 600 570 Z" fill="var(--teal)"/>
      <path d="M470 570 C 620 500, 800 480, 1000 478 L 1000 500 C 820 500, 660 520, 540 570 Z" fill="var(--ribbon-shade)"/>
    </svg>

    <div class="logo-figures" role="img" aria-label="Silhouettes of people from adult to baby walking hand in hand"></div>
    <div class="logo-name">Brightpaths</div>

    <div class="practitioner">
      <p class="practitioner-name">Dorota Valk, <span class="credentials">CCC-SLP, TSSLD</span></p>
      <p class="practitioner-title">Bilingual Speech Language Pathologist</p>
    </div>

    <ul class="contact-list">
      <li>
        <svg viewBox="0 0 24 24"><path fill="var(--teal)" d="M6.6 10.8a15 15 0 0 0 6.6 6.6l2.2-2.2c.3-.3.7-.4 1-.2 1.1.4 2.3.6 3.6.6.6 0 1 .4 1 1V20c0 .6-.4 1-1 1A17 17 0 0 1 3 4c0-.6.4-1 1-1h3.5c.6 0 1 .4 1 1 0 1.3.2 2.5.6 3.6.1.3 0 .7-.2 1Z"/></svg>
        (555) 271-8390.
      </li>
      <li>
        <svg viewBox="0 0 24 24"><rect x="2" y="5" width="20" height="14" rx="1.5" fill="var(--teal)"/><path d="M3 6l9 7 9-7" fill="none" stroke="#fff" stroke-width="1.6"/></svg>
        dorotavalk@brightpathsslp.example
      </li>
      <li>
        <svg viewBox="0 0 24 24" fill="none" stroke="var(--teal)" stroke-width="1.6"><circle cx="12" cy="12" r="9"/><ellipse cx="12" cy="12" rx="4" ry="9"/><path d="M3 12h18M5 7h14M5 17h14"/></svg>
        Brightpathsslp.example
      </li>
    </ul>
  </div>
</body>
</html>
```